Barrowdale Groundworks Business Card Design

We are a new company base in Far North Queensland Australia called Barrowdale Groundworks. We are a company that hire machinery (graders, rollers, excavators and trucks) for road construction and earthworks. We also supply quarry products to the building and construction industries. (Crushed aggregates, road base materials, sand, gravel and rocks). Would like a logo that can also be used on our plant to advertise us.
Target Market(s)
engineers, builders and general public
Industry/Entity Type
Construction
Contact Information for Business Card
Barrowdale Groundworks Pty Ltd, Dennis and Maureen Holt
ABN: 58 302 719 046 ACN: 302 719 046
PO Box 17, Cooktown Qld 4895
Pardoe Street Cooktown Qld 4895

```html
<!DOCTYPE html>
<html lang="en">
<head>
<meta charset="utf-8">
<title>Barrowdale Groundworks Business Card</title>
<link rel="stylesheet" href="https://fonts.googleapis.com/css2?family=Open+Sans:wght@700&family=Arimo:wght@400&display=swap">
<style>
  :root {
    --backdrop: #e9e6e1;
    --strip-green: #3b8d3f;
    --strip-edge: #57a85a;
    --header-blue: #1d6b86;
    --header-blue-dark: #175a72;
    --panel-green: #2f9b4c;
    --panel-green-light: #49b160;
    --road-top: #2a3550;
    --road-mid: #5c6f86;
    --road-bottom: #2b2f33;
    --icon-blue: #3a8fd6;
    --icon-lime: #a7c93a;
    --back-green: #2f8c4b;
    --machine-green: #246f3a;
    --black: #0b0b0b;
    --white: #ffffff;
    --ink: #111111;
  }
  * { box-sizing: border-box; margin: 0; padding: 0; }
  html, body { width: 900px; height: 1200px; overflow: hidden; }
  body {
    background: var(--backdrop);
    font-family: "Arimo", Arial, sans-serif;
    position: relative;
  }
  .card {
    position: absolute;
    left: 100px;
    width: 700px;
    height: 400px;
    overflow: hidden;
    box-shadow: 0 8px 24px rgba(0,0,0,.25);
  }
  .card--front { top: 130px; background: var(--panel-green); }
  .card--back { top: 650px; background: var(--back-green); }

  /* Front */
  .side-strip {
    position: absolute; left: 0; top: 0; width: 112px; height: 100%;
    background: var(--strip-green);
    border-right: 8px solid var(--strip-edge);
    display: flex; align-items: center; justify-content: center;
  }
  .side-strip__name {
    writing-mode: vertical-rl;
    font-family: "Open Sans", Arial, sans-serif;
    font-weight: 700; font-size: 22px; line-height: 1.35;
    color: var(--white); text-transform: uppercase; text-align: center;
  }
  .header {
    position: absolute; left: 112px; top: 0; right: 0; height: 78px;
    background: linear-gradient(180deg, var(--header-blue), var(--header-blue-dark));
    display: flex; align-items: center; gap: 16px; padding-left: 30px;
  }
  .header__names {
    font-family: "Open Sans", Arial, sans-serif; font-weight: 700;
    font-size: 26px; color: var(--white); text-transform: uppercase; letter-spacing: .5px;
  }
  .panel { position: absolute; top: 78px; bottom: 0; }
  .panel--road {
    left: 112px; width: 300px;
    background: linear-gradient(180deg, var(--road-top) 0%, var(--road-mid) 45%, var(--road-bottom) 100%);
  }
  .panel--crew {
    left: 412px; right: 0;
    background: linear-gradient(160deg, var(--panel-green-light), var(--panel-green) 60%);
  }
  .panel__content {
    position: absolute; inset: 0;
    display: flex; flex-direction: column; align-items: center;
    padding: 40px 12px 0; gap: 22px;
    color: var(--white); font-size: 18px; line-height: 1.7; text-align: center;
  }
  .icon-tile { display: flex; gap: 8px; }
  .icon-tile__bar { width: 14px; height: 62px; }
  .icon-tile__box { width: 62px; height: 62px; display: flex; align-items: center; justify-content: center; }
  .icon-tile--blue .icon-tile__bar, .icon-tile--blue .icon-tile__box { background: var(--icon-blue); }
  .icon-tile--lime .icon-tile__bar, .icon-tile--lime .icon-tile__box { background: var(--icon-lime); }

  /* Back */
  .band { position: absolute; left: 0; right: 0; background: var(--black); }
  .band--top { top: 0; height: 62px; }
  .band--bottom { bottom: 0; height: 78px; }
  .machine-art {
    position: absolute; left: 20px; top: 70px; width: 520px; height: 250px;
    background: radial-gradient(ellipse at 50% 55%, var(--machine-green) 0%, rgba(36,111,58,.6) 50%, rgba(47,140,75,0) 75%);
  }
  .name-band {
    position: absolute; left: 0; right: 0; top: 165px; height: 72px;
    background: var(--white);
    display: flex; align-items: center; justify-content: center;
  }
  .name-band__text {
    font-family: "Open Sans", Arial, sans-serif; font-weight: 700;
    font-size: 26px; color: var(--ink); text-transform: uppercase;
  }
</style>
</head>
<body>

<section class="card card--front" aria-label="Business card front">
  <div class="side-strip">
    <p class="side-strip__name">Barrowdale Groundworks<br>Pty Ltd</p>
  </div>

  <header class="header">
    <svg width="34" height="36" viewBox="0 0 34 36" aria-hidden="true">
      <circle cx="17" cy="10" r="8" fill="#ffffff"/>
      <path d="M2 36 C2 24 9 20 17 20 C25 20 32 24 32 36 Z" fill="#ffffff"/>
      <path d="M17 21 L14 26 L17 34 L20 26 Z" fill="#1d6b86"/>
    </svg>
    <h1 class="header__names">Dennis and Maureen Holt</h1>
  </header>

  <div class="panel panel--road" role="img" aria-label="Photo of an open highway at dusk">
    <div class="panel__content">
      <div class="icon-tile icon-tile--blue">
        <span class="icon-tile__bar"></span>
        <span class="icon-tile__box">
          <svg width="34" height="34" viewBox="0 0 24 24" aria-hidden="true">
            <path fill="#ffffff" d="M6.6 10.8c1.4 2.8 3.8 5.1 6.6 6.6l2.2-2.2c.3-.3.7-.4 1-.2 1.1.4 2.3.6 3.6.6.6 0 1 .4 1 1V20c0 .6-.4 1-1 1C10.6 21 3 13.4 3 4c0-.6.4-1 1-1h3.5c.6 0 1 .4 1 1 0 1.3.2 2.5.6 3.6.1.3 0 .7-.2 1L6.6 10.8z"/>
          </svg>
        </span>
      </div>
      <p class="contact">ABN: 58 302 719 046<br>ACN: 302 719 046</p>
    </div>
  </div>

  <div class="panel panel--crew" role="img" aria-label="Faint photo of construction workers on site">
    <div class="panel__content">
      <div class="icon-tile icon-tile--lime">
        <span class="icon-tile__bar"></span>
        <span class="icon-tile__box">
          <svg width="30" height="40" viewBox="0 0 24 32" aria-hidden="true">
            <path fill="#ffffff" d="M12 0C5.4 0 0 5.2 0 11.7 0 20.5 12 32 12 32s12-11.5 12-20.3C24 5.2 18.6 0 12 0zm0 16.5a5 5 0 1 1 0-10 5 5 0 0 1 0 10z"/>
          </svg>
        </span>
      </div>
      <p class="address">PO Box 17, Tarrengo Qld<br>4872 Pardoe Street<br>Tarrengo Qld 4872</p>
    </div>
  </div>
</section>

<section class="card card--back" aria-label="Business card back">
  <div class="band band--top"></div>
  <div class="machine-art" role="img" aria-label="Illustration of a tracked excavator with raised arm and bucket"></div>
  <div class="name-band">
    <h2 class="name-band__text">Barrowdale Groundworks Pty Ltd</h2>
  </div>
  <div class="band band--bottom"></div>
</section>

</body>
</html>
```